We need a design to be used to promote a Black Friday sale in an optical dispensary. This will be used as an email campaign, point of sale materials including counter cards and window cling.

The email graphic needs to be 4" wide by 6" deep, the counter cards are 9" wide by 6" counter cards and a 16" wide by 20" deep window cling.

The content of the design should include:
1. Offer of 50% Off the price of any BLACK frame with the purchase of prescription lenses all day on Black Friday, November 28.
2. Free lens cleaning solution refills for life

Store Locations:

Meridian Lens Works
18350 Larkspur Pkwy
Rosenberg, TX 77471
281-617-2048
www.larkspurmlw.example

Meridian Lens Works
4817 Cedar Bend Road
Houston TX 77082
(281) 752-3390
www.cedarbendmlw.example

The design should be contemporary and fun, and tie into a "black friday theme" Please incorporate the attached MLW (Meridian Lens Works) logo

```html
<!DOCTYPE html>
<html lang="en">
<head>
<meta charset="utf-8">
<title>Black Friday Sale – Meridian Lens Works</title>
<link rel="stylesheet" href="https://fonts.googleapis.com/css2?family=Archivo+Black&family=Arimo:wght@400;700&display=swap">
<style>
  :root {
    --ink: #231f20;
    --paper: #ffffff;
    --canvas: #ffffff;
    --skin-light: #e9cbb8;
    --skin-mid: #d6a98f;
    --hair: #4a3127;
    --baby-light: #f2d9cc;
    --baby-mid: #e3b8a4;
  }
  html, body {
    margin: 0;
    padding: 0;
    overflow: hidden;
    background: var(--canvas);
  }
  .canvas {
    position: relative;
    width: 1200px;
    height: 1000px;
    overflow: hidden;
    background: var(--canvas);
  }
  .panel {
    position: absolute;
    display: block;
    background: var(--paper);
  }
  .panel--email   { left: 41px;  top: 233px; width: 360px; height: 502px; }
  .panel--counter { left: 431px; top: 233px; width: 340px; height: 502px; }
  .panel--window  { left: 812px; top: 245px; width: 343px; height: 502px; }
  .headline { font-family: "Archivo Black", "Arial Black", sans-serif; }
  .body     { font-family: "Arimo", Arial, sans-serif; }
  .bold     { font-weight: 700; }
  .ink   { fill: var(--ink); }
  .paper { fill: var(--paper); }
  .brand-name { font-family: "Archivo Black", "Arial Black", sans-serif; fill: var(--ink); }
</style>
</head>
<body>
<main class="canvas">

  <!-- Email / portrait flyer -->
  <svg class="panel panel--email" viewBox="0 0 360 502" xmlns="http://www.w3.org/2000/svg">
    <defs>
      <linearGradient id="portrait-tone-a" x1="0" y1="0" x2="1" y2="0">
        <stop offset="0" stop-color="var(--hair)"/>
        <stop offset="0.35" stop-color="var(--skin-mid)"/>
        <stop offset="0.7" stop-color="var(--skin-light)"/>
        <stop offset="1" stop-color="var(--hair)"/>
      </linearGradient>
    </defs>
    <rect class="ink" x="0" y="4" width="360" height="6"/>
    <rect class="paper" x="144" y="-2" width="90" height="30"/>
    <text class="brand-name" x="189" y="22" font-size="22" text-anchor="middle">MLW</text>

    <rect x="0" y="35" width="170" height="467" fill="url(#portrait-tone-a)" role="img" aria-label="Portrait photo of a woman wearing black-framed glasses"/>

    <text class="headline ink" x="178" y="100" font-size="48" textLength="164" lengthAdjust="spacingAndGlyphs">BLACK</text>
    <text class="headline ink" x="178" y="148" font-size="48" textLength="164" lengthAdjust="spacingAndGlyphs">FRIDAY</text>

    <g class="offer-sale">
      <circle class="ink" cx="253" cy="254" r="98"/>
      <text class="headline paper" x="202" y="217" font-size="30" textLength="86" lengthAdjust="spacingAndGlyphs">SALE</text>
      <text class="headline paper" x="188" y="276" font-size="60" textLength="118" lengthAdjust="spacingAndGlyphs">50%</text>
      <text class="headline paper" x="308" y="249" font-size="15" textLength="34" lengthAdjust="spacingAndGlyphs">OFF</text>
      <text class="body paper" x="270" y="291" font-size="5.5" text-anchor="middle" textLength="136" lengthAdjust="spacingAndGlyphs">Any BLACK frame with the purchase of prescription lenses all day</text>
      <text class="body bold paper" x="270" y="305" font-size="11" text-anchor="middle">Friday, November 28.</text>
    </g>

    <g class="store-list body paper" font-size="6.5" text-anchor="middle">
      <circle class="ink" cx="149" cy="386" r="70"/>
      <text x="149" y="346">Meridian Lens Works</text>
      <text x="149" y="354">18350 Larkspur Pkwy</text>
      <text x="149" y="362">Rosenberg, TX 77471</text>
      <text x="149" y="370">281-617-2048</text>
      <text x="149" y="378" font-size="5.5" textLength="86" lengthAdjust="spacingAndGlyphs">www.larkspurmlw.example</text>
      <text x="149" y="397">Meridian Lens Works</text>
      <text x="149" y="405">4817 Cedar Bend Road</text>
      <text x="149" y="413">Houston TX 77082</text>
      <text x="149" y="421">(281) 752-3390</text>
      <text x="149" y="429" font-size="5.5" textLength="86" lengthAdjust="spacingAndGlyphs">www.cedarbendmlw.example</text>
    </g>

    <g class="offer-free">
      <circle class="ink" cx="281" cy="382" r="68"/>
      <text class="headline paper" x="281" y="389" font-size="30" text-anchor="middle" textLength="96" lengthAdjust="spacingAndGlyphs">FREE</text>
      <text class="body paper" x="281" y="405" font-size="9" text-anchor="middle">lens cleaning solution</text>
      <text class="body paper" x="281" y="416" font-size="9" text-anchor="middle">refills for life</text>
    </g>
  </svg>

  <!-- Counter card -->
  <svg class="panel panel--counter" viewBox="0 0 340 502" xmlns="http://www.w3.org/2000/svg">
    <defs>
      <radialGradient id="baby-tone" cx="0.45" cy="0.55" r="0.7">
        <stop offset="0" stop-color="var(--baby-light)"/>
        <stop offset="1" stop-color="var(--baby-mid)"/>
      </radialGradient>
    </defs>
    <polygon class="ink" points="0,0 50,0 36,502 0,502"/>
    <text class="brand-name" x="194" y="40" font-size="22" text-anchor="middle">MLW</text>

    <rect x="36" y="265" width="304" height="237" fill="url(#baby-tone)" role="img" aria-label="Photo of a baby wearing oversized black glasses"/>

    <g class="offer-sale">
      <circle class="ink" cx="134" cy="142" r="85"/>
      <text class="headline paper" x="86" y="124" font-size="30" textLength="92" lengthAdjust="spacingAndGlyphs">SALE</text>
      <text class="headline paper" x="64" y="178" font-size="52" textLength="112" lengthAdjust="spacingAndGlyphs">50%</text>
      <text class="headline paper" x="176" y="157" font-size="13" textLength="30" lengthAdjust="spacingAndGlyphs">OFF</text>
      <text class="body paper" x="134" y="199" font-size="6.5" text-anchor="middle">Any BLACK frame with the purchase of</text>
      <text class="body paper" x="134" y="208" font-size="6.5" text-anchor="middle">prescription lenses all day</text>
    </g>

    <g class="offer-free">
      <circle class="ink" cx="259" cy="96" r="60"/>
      <text class="headline paper" x="259" y="102" font-size="21" text-anchor="middle" textLength="62" lengthAdjust="spacingAndGlyphs">FREE</text>
      <text class="body paper" x="259" y="115" font-size="7.5" text-anchor="middle">lens cleaning solution</text>
      <text class="body paper" x="259" y="124" font-size="7.5" text-anchor="middle">refills for life</text>
    </g>

    <g class="store-list body paper" font-size="5" text-anchor="middle">
      <circle class="ink" cx="254" cy="187" r="55"/>
      <text x="254" y="158">Meridian Lens Works</text>
      <text x="254" y="164">18350 Larkspur Pkwy</text>
      <text x="254" y="170">Rosenberg, TX 77471</text>
      <text x="254" y="176">281-617-2048</text>
      <text x="254" y="182">www.larkspurmlw.example</text>
      <text x="254" y="192">Meridian Lens Works</text>
      <text x="254" y="198">4817 Cedar Bend Road</text>
      <text x="254" y="204">Houston TX 77082</text>
      <text x="254" y="210">(281) 752-3390</text>
      <text x="254" y="216">www.cedarbendmlw.example</text>
    </g>

    <text class="headline ink" x="60" y="249" font-size="8">FRIDAY</text>
    <text class="headline ink" x="60" y="263" font-size="14">NOVEMBER 28</text>

    <g class="price-tag" transform="translate(200,262) rotate(62)">
      <polygon class="ink" points="0,-22 110,-22 128,0 110,22 0,22"/>
      <circle class="paper" cx="114" cy="0" r="3"/>
      <text class="headline paper" x="8" y="-3" font-size="18">BLACK</text>
      <text class="headline paper" x="8" y="17" font-size="18">FRIDAY</text>
    </g>
  </svg>

  <!-- Window cling -->
  <svg class="panel panel--window" viewBox="0 0 343 502" xmlns="http://www.w3.org/2000/svg">
    <defs>
      <linearGradient id="portrait-tone-b" x1="0" y1="0" x2="1" y2="0">
        <stop offset="0" stop-color="var(--hair)"/>
        <stop offset="0.35" stop-color="var(--skin-mid)"/>
        <stop offset="0.75" stop-color="var(--skin-light)"/>
        <stop offset="1" stop-color="var(--hair)"/>
      </linearGradient>
    </defs>
    <rect class="ink" x="0" y="34" width="343" height="6"/>
    <rect class="paper" x="133" y="24" width="90" height="30"/>
    <text class="brand-name" x="178" y="48" font-size="22" text-anchor="middle">MLW</text>

    <rect x="0" y="75" width="160" height="427" fill="url(#portrait-tone-b)" role="img" aria-label="Portrait photo of a woman wearing black-framed glasses"/>

    <line x1="162" y1="123" x2="330" y2="100" stroke="var(--ink)" stroke-width="1.5"/>
    <line x1="162" y1="205" x2="343" y2="180" stroke="var(--ink)" stroke-width="1.5"/>
    <g transform="rotate(-6 255 160)">
      <text class="headline ink" x="187" y="145" font-size="34" textLength="136" lengthAdjust="spacingAndGlyphs">BLACK</text>
      <text class="headline ink" x="187" y="182" font-size="34" textLength="140" lengthAdjust="spacingAndGlyphs">FRIDAY</text>
    </g>

    <polygon class="ink" points="273,210 343,280 343,502 0,502 0,435"/>

    <text class="body bold paper" x="248" y="257" font-size="10" text-anchor="middle">Friday</text>
    <text class="body bold paper" x="248" y="268" font-size="10" text-anchor="middle">November 28.</text>
    <text class="headline paper" x="244" y="322" font-size="48" text-anchor="middle" textLength="134" lengthAdjust="spacingAndGlyphs">SALE</text>
    <text class="headline paper" x="244" y="376" font-size="54" text-anchor="middle" textLength="118" lengthAdjust="spacingAndGlyphs">50%</text>
    <text class="body paper" x="244" y="391" font-size="6.5" text-anchor="middle">Any BLACK frame with the purchase of prescription lenses all day</text>
    <text class="body paper" x="210" y="416" font-size="12" text-anchor="middle"><tspan class="bold">FREE</tspan> lens cleaning solution refills for life</text>

    <g class="store-list body paper" font-size="8" text-anchor="middle">
      <text x="138" y="446">Meridian Lens Works</text>
      <text x="138" y="455">18350 Larkspur Pkwy</text>
      <text x="138" y="464">Rosenberg, TX 77471</text>
      <text x="138" y="473">281-617-2048</text>
      <text x="138" y="482" font-size="6.5" letter-spacing="1">www.larkspurmlw.example</text>
      <text x="270" y="446">Meridian Lens Works</text>
      <text x="270" y="455">4817 Cedar Bend Road</text>
      <text x="270" y="464">Houston TX 77082</text>
      <text x="270" y="473">(281) 752-3390</text>
      <text x="270" y="482" font-size="6.5" letter-spacing="1">www.cedarbendmlw.example</text>
    </g>
  </svg>

</main>
</body>
</html>
```